Brackwell Powerpoint Template

We need a .pptx template for company presentations.

It is comprised of only two pages:

1) cover page
2) inside pages

Both pages should be based on our logo, attached on the brief.

The cover page must have space for title and subtitle.
Updates

Update on the brief:

We are looking for a cover page that is not too "busy" or complicated. Dark background is preferred, especially if it plays with the logo colors (maybe playing with a negative version of it).

The inside page has also to be simple: no arrows or anything similar. Keep in mind that those presentations will be printed in paper.

The inside page should have the logo either on the top right corner or on the bottom right corner.

A good way to separate the title (or to create space for it) would be to play with the horizon line from the logo maybe a thinner version of it, since it will have to be much longer).

The inside page must have a white background and a place for the page number.

Target Market(s)

High end investors

Industry/Entity Type

It Company

```html
<!DOCTYPE html>
<html lang="en">
<head>
<meta charset="utf-8">
<title>Brackwell Capital Partners – Closing Slide</title>
<link href="https://fonts.googleapis.com/css2?family=Carlito:ital,wght@0,400;0,700;1,700&display=swap" rel="stylesheet">
<style>
  :root {
    --stage: #d4d4d4;
    --blue-top: #2a8ad6;
    --blue-mid: #1c66b0;
    --navy: #06203d;
    --title-cyan: #86def8;
    --white: #ffffff;
    --ink: #111111;
    --link: #2f4fd8;
    --brand: #2f6580;
    --strip: #2a8ad6;
  }
  * { margin: 0; padding: 0; box-sizing: border-box; }
  html, body {
    width: 1200px; height: 952px; overflow: hidden;
    background: var(--stage);
    font-family: "Carlito", "Calibri", sans-serif;
  }
  .slide {
    position: absolute; left: 96px; top: 96px;
    width: 990px; height: 741px; overflow: hidden;
    background: linear-gradient(180deg, var(--blue-top) 0%, var(--blue-top) 22%, var(--blue-mid) 52%, var(--navy) 78%);
  }
  .slide__shapes { position: absolute; inset: 0; }
  .slide__kicker {
    position: absolute; left: 77px; top: 112px;
    color: var(--white); font-weight: 700; font-style: italic; font-size: 28px;
  }
  .slide__title {
    position: absolute; left: 76px; top: 148px;
    color: var(--title-cyan); font-weight: 400; font-size: 64px; line-height: 67px;
  }
  .contact {
    position: absolute; left: 42px; top: 556px;
    font-size: 13px; line-height: 20px; color: var(--ink);
    list-style: none;
  }
  .contact__name, .contact__web { font-weight: 700; }
  .contact__email { color: var(--link); text-decoration: underline; }
  .social {
    position: absolute; left: 42px; top: 676px;
    display: flex; gap: 5px;
  }
  .social__tile { width: 17px; height: 17px; background: var(--ink); border-radius: 2px; }
  .brand {
    position: absolute; left: 596px; top: 588px; width: 320px;
    text-align: center; color: var(--brand); font-weight: 400;
  }
  .brand__name { font-size: 50px; letter-spacing: 5px; line-height: 52px; }
  .brand__sub { font-size: 19px; letter-spacing: 8px; line-height: 26px; }
  .slide__strip {
    position: absolute; left: 0; bottom: 0; width: 100%; height: 29px;
    background: var(--strip);
  }
</style>
</head>
<body>
  <main class="slide">
    <svg class="slide__shapes" width="990" height="741" viewBox="0 0 990 741" aria-hidden="true">
      <defs>
        <linearGradient id="swoosh" x1="0" y1="0" x2="1" y2="0">
          <stop offset="0" stop-color="#6d7c89"/>
          <stop offset="0.35" stop-color="#aab4bc"/>
          <stop offset="0.6" stop-color="#ffffff"/>
        </linearGradient>
      </defs>
      <path d="M0,488 C160,468 320,448 528,445 C700,442 850,468 990,493 L990,741 L0,741 Z" fill="url(#swoosh)"/>
      <path d="M0,546 C160,492 330,449 528,445 C700,442 850,468 990,493 L990,741 L0,741 Z" fill="#ffffff"/>
    </svg>

    <p class="slide__kicker">&gt;&gt; Moving forward.</p>
    <h1 class="slide__title">Where do you feel<br>we go from here?</h1>

    <ul class="contact">
      <li class="contact__name">Name</li>
      <li class="contact__role">Title</li>
      <li class="contact__phone">(XXX) XXX.XXXX</li>
      <li class="contact__email">jdoe@brackwell.com</li>
      <li class="contact__web">www.brackwell.com</li>
    </ul>
    <div class="social" aria-label="Social links">
      <span class="social__tile"></span>
      <span class="social__tile"></span>
      <span class="social__tile"></span>
    </div>

    <div class="brand">
      <div class="brand__name">BRACKWELL</div>
      <div class="brand__sub">CAPITAL PARTNERS</div>
    </div>

    <div class="slide__strip"></div>
  </main>
</body>
</html>
```